Kitchen Tools Infographic - Helpful Items for Healthy Home Meals

We are a weight loss company that provides holistic, natural nutrition programs to consumers -- you can see our web site at www.FernQuill.com. We need a simple infographic to be shared on social media and via email. The topic for the infographic is "Equip Your Kitchen for Healthy Home Meals". We've outlined 5 groups of kitchen tools that are helpful for consumers to have for preparing home meals, and included some framing statistics emphasizing the weight management benefits of preparing meals versus eating out.

Target Market(s)

Women age 35-55

Industry/Entity Type

Health And Wellness

Font styles to use
Sans Serif

Colors
0292cd
9bcb3b

Requirements
Must have
• - FernQuill Logo
• - Graphics summarizing statistic (weight gain)
• - Graphics showing groupings of kitchen tools
Should not have
• body scale graphics
• before/after graphics

```html
<!DOCTYPE html>
<html lang="en">
<head>
<meta charset="utf-8">
<title>Equip Your Kitchen for Healthy Home Meals – FernQuill</title>
<link href="https://fonts.googleapis.com/css2?family=Anton&family=Bebas+Neue&family=Yellowtail&family=Source+Sans+3:wght@400;600;700&family=Open+Sans:wght@400;600;700&display=swap" rel="stylesheet">
<style>
  :root{
    --brand-blue:#0292cd;
    --brand-green:#9bcb3b;
    --teal:#2e9cbd;
    --teal-dark:#1f7f9c;
    --ribbon:#3aa7c4;
    --ribbon-shade:#1b5d72;
    --tool-blue:#3aaccc;
    --tool-green:#7dc42a;
    --olive:#4d6b1a;
    --bar-light:#d0e177;
    --bar-mid:#b2c452;
    --bar-dark:#6f9a2c;
    --pie-light:#9bcb3b;
    --pie-dark:#6f9a2c;
    --ink:#2b3a44;
    --rule:#8cc43a;
    --outline:#23505e;
  }
  *{margin:0;padding:0;box-sizing:border-box}
  html,body{width:1200px;height:1200px;overflow:hidden}
  body{
    position:relative;
    font-family:"Source Sans 3",sans-serif;
    background:linear-gradient(180deg,#78c3d6 0px,#c4e5ee 180px,#ffffff 290px,#ffffff 1000px,#c8e6ef 1070px,#6cbdd4 1200px);
  }
  .abs{position:absolute}
  .ribbon{left:0;top:0;width:1200px;height:220px}
  .title-main{left:242px;width:748px;top:62px;text-align:center;font-family:"Bebas Neue",sans-serif;font-size:50px;color:#fff;letter-spacing:1px;line-height:1;white-space:nowrap}
  .title-script{left:242px;width:748px;top:104px;text-align:center;font-family:"Yellowtail",cursive;font-size:46px;color:#fff;line-height:1.1;white-space:nowrap}
  .why{left:340px;top:182px;width:580px;color:var(--ink);font-family:"Open Sans",sans-serif}
  .why h2{font-size:19px;font-weight:600}
  .why p{font-size:12.5px;line-height:1;text-indent:48px;margin-top:2px}
  .rule-h{height:1px;background:var(--rule)}
  .rule-v{width:1px;background:var(--rule)}
  .rule-v.dark{background:#6f9a2c}
  .chart-title{font-family:"Open Sans",sans-serif;font-weight:600;font-size:15px;color:var(--olive);text-align:center}
  .legend{font-family:"Open Sans",sans-serif;font-size:14px;color:var(--olive);display:flex;align-items:center;gap:8px;white-space:nowrap}
  .swatch{width:13px;height:13px;display:inline-block}
  .dot{width:15px;height:15px;border-radius:50%;display:inline-block}
  .bar-label{font-family:"Open Sans",sans-serif;font-size:11.5px;color:var(--bar-dark)}
  .tools-heading{left:0;width:1210px;top:554px;text-align:center;font-family:"Open Sans",sans-serif;font-weight:600;font-size:19px;color:var(--teal)}
  .group-num{width:39px;height:39px;border-radius:50%;color:#fff;font-family:"Open Sans",sans-serif;font-weight:700;font-size:20px;display:flex;align-items:center;justify-content:center}
  .group-num.blue{background:var(--tool-blue)}
  .group-num.green{background:var(--tool-green)}
  .group-name{font-family:"Open Sans",sans-serif;font-weight:600;font-size:20px}
  .blue-t{color:var(--tool-blue)}
  .green-t{color:var(--tool-green)}
  .tool-list{list-style:none;font-weight:600;font-size:14.5px;letter-spacing:-0.2px}
  .tool-list li{height:26px;line-height:18px;display:flex;align-items:flex-start;gap:6px;white-space:nowrap}
  .tool-icon{display:inline-block;border-radius:3px;flex:none}
  .tool-icon.blue{background:var(--tool-blue)}
  .tool-icon.green{background:var(--tool-green)}
  .footer-rule{left:64px;top:1080px;width:880px;height:1px;background:var(--rule)}
  .cta-line{left:94px;top:1106px;font-family:"Anton",sans-serif;font-size:32px;color:#fff;letter-spacing:0.2px;white-space:nowrap;
    text-shadow:-1.5px -1.5px 0 var(--outline),1.5px -1.5px 0 var(--outline),-1.5px 1.5px 0 var(--outline),1.5px 1.5px 0 var(--outline)}
  .invite{right:472px;top:1152px;font-family:"Yellowtail",cursive;font-size:28px;line-height:1;color:#fff;white-space:nowrap;
    text-shadow:-1px -1px 0 var(--outline),1px -1px 0 var(--outline),-1px 1px 0 var(--outline),1px 1px 0 var(--outline)}
  .contact-btn{left:740px;top:1154px;width:150px;height:33px;background:var(--tool-green);border:2px solid #fff;border-radius:3px;color:#fff;
    font-family:"Open Sans",sans-serif;font-weight:700;font-size:17px;display:flex;align-items:center;justify-content:center;white-space:nowrap}
  .brand{left:952px;top:1088px;width:240px;display:flex;align-items:center;gap:10px;font-family:"Open Sans",sans-serif;font-weight:700;font-size:36px;color:var(--brand-green);white-space:nowrap}
  .brand .mark{width:22px;height:22px;border-radius:50%;background:var(--brand-green)}
</style>
</head>
<body>

<svg class="abs ribbon" viewBox="0 0 1200 220" aria-hidden="true">
  <polygon points="132,80 328,80 328,198 132,198 164,139" fill="var(--teal-dark)"/>
  <polygon points="1102,80 906,80 906,198 1102,198 1070,139" fill="var(--teal-dark)"/>
  <polygon points="242,178 328,178 328,198" fill="var(--ribbon-shade)"/>
  <polygon points="990,178 906,178 906,198" fill="var(--ribbon-shade)"/>
  <rect x="242" y="56" width="748" height="122" fill="var(--ribbon)"/>
</svg>
<div class="abs title-main">EQUIP YOUR KITCHEN</div>
<div class="abs title-script">for Healthy Home Meals</div>

<section class="abs why">
  <h2>Why Cook at Home?</h2>
  <p>Those who eat out consume an average of 134 calories more per meal. Americans eat out an average of 4.5 times per week, so those extra calories can add up to substantial weight gain -- and give you a reason to prepare your own meals.</p>
</section>

<div class="abs rule-h" style="left:40px;top:262px;width:1120px"></div>

<div class="abs chart-title" style="left:110px;width:400px;top:296px">Excess Calories from Restaurant Meals</div>
<svg class="abs" style="left:0;top:0" width="600" height="520" aria-label="Pie chart: 600 calories per week, 100 calories per meal">
  <circle cx="308" cy="400" r="70" fill="var(--pie-light)"/>
  <path d="M308,400 L353,346.4 A70,70 0 0 1 378,401.7 Z" fill="var(--pie-dark)"/>
  <text x="354" y="383" font-family="Open Sans,sans-serif" font-size="12" fill="#fff" text-anchor="middle">100</text>
  <text x="264" y="422" font-family="Open Sans,sans-serif" font-size="12" fill="#fff" text-anchor="middle">600</text>
</svg>
<div class="abs legend" style="left:132px;top:483px"><span class="swatch" style="background:var(--pie-light)"></span>Calories Per Week</div>
<div class="abs legend" style="left:364px;top:483px"><span class="swatch" style="background:var(--pie-dark)"></span>Calories Per Meal</div>

<div class="abs rule-v dark" style="left:598px;top:292px;height:209px"></div>

<div class="abs chart-title" style="left:687px;width:400px;top:296px">Pounds Gained from Restaurant Meals</div>
<svg class="abs" style="left:600px;top:330px" width="600" height="120" aria-label="Bar chart: 8.96 lbs in 1 year, 4.50 lbs in 6 months, 1.40 lbs in 2 months">
  <rect x="68" y="12" width="396" height="22" fill="var(--bar-light)"/>
  <rect x="68" y="52" width="261" height="21" fill="var(--bar-mid)"/>
  <line x1="334" y1="63" x2="462" y2="63" stroke="var(--bar-dark)"/>
  <rect x="68" y="88" width="73" height="21" fill="var(--bar-dark)"/>
  <line x1="150" y1="99" x2="462" y2="99" stroke="var(--bar-dark)"/>
</svg>
<div class="abs bar-label" style="left:1070px;top:346px">8.96 lbs</div>
<div class="abs bar-label" style="left:1070px;top:385px">4.50 lbs</div>
<div class="abs bar-label" style="left:1070px;top:421px">1.40 lbs</div>
<div class="abs legend" style="left:730px;top:480px"><span class="dot" style="background:var(--bar-light)"></span>1 year</div>
<div class="abs legend" style="left:819px;top:480px"><span class="dot" style="background:var(--bar-mid)"></span>6 months</div>
<div class="abs legend" style="left:920px;top:480px"><span class="dot" style="background:var(--bar-dark)"></span>2 months</div>

<div class="abs rule-h" style="left:40px;top:542px;width:1120px"></div>

<div class="abs tools-heading">Make healthy eating easier with these kitchen tools:</div>

<div class="abs group-num blue" style="left:41px;top:585px">1</div>
<div class="abs group-name blue-t" style="left:87px;top:591px">PREP:</div>
<ul class="abs tool-list" style="left:122px;top:617px">
  <li class="blue-t">Essential for prepping meat and vegetables. <span class="tool-icon blue" role="img" aria-label="cutting board icon" style="width:42px;height:20px"></span></li>
  <li class="green-t">Go for quality to make chopping, dicing and slicing faster and easier. <span class="tool-icon green" role="img" aria-label="chef knife icon" style="width:38px;height:12px"></span></li>
  <li class="blue-t">Get the precision you need for perfect recipes and portion control. <span class="tool-icon blue" role="img" aria-label="kitchen scale icon" style="width:30px;height:24px"></span></li>
</ul>

<div class="abs rule-v" style="left:602px;top:606px;height:126px"></div>

<div class="abs group-num blue" style="left:631px;top:585px">2</div>
<div class="abs group-name blue-t" style="left:677px;top:591px">TECH:</div>
<ul class="abs tool-list" style="left:711px;top:617px">
  <li class="blue-t">Make highly nutritious, healthy drinks from fruits and veggies.</li>
  <li class="green-t">Cook delicious meals while you are at work.</li>
  <li class="blue-t">Create single pot meals in 20 minutes or less.</li>
</ul>
<span class="abs tool-icon blue" role="img" aria-label="blender icon" style="left:1106px;top:592px;width:26px;height:54px"></span>
<span class="abs tool-icon green" role="img" aria-label="slow cooker icon" style="left:992px;top:636px;width:34px;height:32px"></span>
<span class="abs tool-icon blue" role="img" aria-label="pressure cooker icon" style="left:1010px;top:664px;width:54px;height:32px"></span>

<div class="abs rule-h" style="left:260px;top:732px;width:648px"></div>

<div class="abs group-num green" style="left:297px;top:751px">3</div>
<div class="abs group-name green-t" style="left:343px;top:757px">COOK:</div>
<ul class="abs tool-list" style="left:378px;top:782px">
  <li class="green-t">Nonstick cooking surface allows you to cook without oil</li>
  <li class="blue-t">Preserve nutrients and natural, fresh taste. <span class="tool-icon blue" role="img" aria-label="steamer icon" style="width:30px;height:34px;margin-top:-10px"></span></li>
  <li class="green-t">Ideal for roasting vegetables in the oven or baking chicken and fish dishes <span class="tool-icon green" role="img" aria-label="baking dish icon" style="width:66px;height:14px;margin-left:4px"></span></li>
</ul>
<span class="abs tool-icon green" role="img" aria-label="nonstick pan icon" style="left:734px;top:802px;width:50px;height:30px;border-radius:15px"></span>

<div class="abs rule-v" style="left:606px;top:872px;height:36px"></div>
<div class="abs rule-h" style="left:166px;top:906px;width:389px"></div>
<div class="abs rule-h" style="left:646px;top:905px;width:386px"></div>

<div class="abs group-num blue" style="left:41px;top:915px">4</div>
<div class="abs group-name blue-t" style="left:87px;top:921px">SERVE:</div>
<ul class="abs tool-list" style="left:122px;top:948px">
  <li class="blue-t">To reduce waste and dress up your table <span class="tool-icon blue" role="img" aria-label="placemat icon" style="width:36px;height:28px;margin-top:-8px"></span></li>
  <li class="green-t">Pre-plate meals rather than serving family style to control portions <span class="tool-icon green" role="img" aria-label="plate and cutlery icon" style="width:58px;height:30px;border-radius:15px;margin-top:-6px"></span></li>
  <li class="blue-t">Use salad plates and smaller dishware to manage perception of food volume <span class="tool-icon blue" role="img" aria-label="small plates icon" style="width:56px;height:20px;border-radius:10px"></span></li>
</ul>

<div class="abs group-num blue" style="left:631px;top:915px">5</div>
<div class="abs group-name blue-t" style="left:677px;top:921px">STORE:</div>
<ul class="abs tool-list" style="left:711px;top:948px">
  <li class="blue-t">Keep your healthy leftovers so nothing goes to waste. <span class="tool-icon blue" role="img" aria-label="storage jar icon" style="width:24px;height:34px;margin-top:-10px"></span></li>
  <li class="green-t">Perfect for premade salads that you can bring to work. <span class="tool-icon green" role="img" aria-label="salad container icon" style="width:18px;height:26px;margin-top:-4px"></span></li>
  <li class="blue-t">Prepare double batches to make the most of your time. <span class="tool-icon blue" role="img" aria-label="freezer container icon" style="width:24px;height:22px"></span></li>
</ul>

<div class="abs footer-rule"></div>
<div class="abs cta-line">FERNQUILL CAN HELP YOU DEVELOP HEALTHIER EATING HABITS.</div>
<div class="abs invite">We invite you to learn more.</div>
<div class="abs contact-btn">CONTACT US</div>
<div class="abs brand"><span class="mark"></span>FernQuill</div>

</body>
</html>
```